Product packaging design for lentils

Looking to create a design for lentils in 4lb format. We are looking to create a base design for the bags, and then from there will have additional designs for the different products with different product name, barcodes and nutritional information.

Industry/Entity Type

Food

```html
<!DOCTYPE html>
<html lang="en">
<head>
<meta charset="utf-8">
<title>Greenmeadow Whole Red Lentils – 4lb Bag</title>
<link href="https://fonts.googleapis.com/css2?family=Roboto+Slab:wght@700&display=swap" rel="stylesheet">
<style>
  :root {
    --forest: #006837;
    --forest-deep: #005c30;
    --leaf: #7ab13a;
    --lentil: #e8682a;
    --lentil-light: #f08a45;
    --lentil-dark: #d4561c;
    --label-white: #e8e8e8;
    --page: #ffffff;
    --cert-navy: #1d4f91;
  }
  html, body {
    margin: 0;
    padding: 0;
    width: 1200px;
    height: 1200px;
    overflow: hidden;
    background: var(--page);
  }
  .package {
    display: block;
    width: 1200px;
    height: 1200px;
  }
  .brand-name,
  .label-text {
    font-family: "Roboto Slab", serif;
    font-weight: 700;
  }
</style>
</head>
<body>
<svg class="package" viewBox="0 0 1200 1200" xmlns="http://www.w3.org/2000/svg">
  <defs>
    <linearGradient id="lentilTone" x1="0" y1="0" x2="1" y2="1">
      <stop offset="0" stop-color="var(--lentil-light)"/>
      <stop offset="0.5" stop-color="var(--lentil)"/>
      <stop offset="1" stop-color="var(--lentil-dark)"/>
    </linearGradient>
  </defs>

  <!-- product photo area -->
  <rect class="product-photo" x="241" y="272" width="703" height="716" fill="url(#lentilTone)"
        role="img" aria-label="Close-up photograph of whole red lentils filling the bag front"/>

  <!-- top band -->
  <path class="band-top" d="M206 153 H988 V185 L944 272 H241 L206 185 Z" fill="var(--forest)"/>
  <rect class="stripe-top" x="241" y="272" width="703" height="9" fill="var(--leaf)"/>

  <!-- bottom band -->
  <rect class="stripe-bottom" x="241" y="983" width="703" height="9" fill="var(--leaf)"/>
  <path class="band-bottom" d="M241 992 H944 L1000 1076 H198 Z" fill="var(--forest)"/>

  <!-- main label panel -->
  <path class="label-panel"
        d="M432 503 H765 Q831 503 831 570 V760 Q831 820 770 820 H728 V852 Q728 872 708 872 H640 L600 912 L560 872 H489 Q469 872 469 852 V820 H427 Q366 820 366 760 V570 Q366 503 432 503 Z"
        fill="var(--forest-deep)" stroke="var(--leaf)" stroke-width="7" stroke-linejoin="round"/>

  <!-- brand mark -->
  <circle class="brand-disc" cx="600" cy="470" r="108" fill="var(--leaf)" stroke="var(--forest-deep)" stroke-width="7"/>
  <text class="brand-name" x="600" y="486" text-anchor="middle" font-size="32"
        textLength="180" lengthAdjust="spacingAndGlyphs" fill="var(--forest-deep)">Greenmeadow</text>

  <!-- label copy -->
  <text class="label-text tagline" x="600" y="622" text-anchor="middle" font-size="34"
        textLength="326" lengthAdjust="spacingAndGlyphs" fill="var(--leaf)">PREMIUM QUALITY</text>
  <text class="label-text product-name" x="600" y="694" text-anchor="middle" font-size="68"
        textLength="400" lengthAdjust="spacingAndGlyphs" fill="var(--label-white)">WHOLE RED</text>
  <text class="label-text product-name" x="600" y="764" text-anchor="middle" font-size="68"
        textLength="282" lengthAdjust="spacingAndGlyphs" fill="var(--label-white)">LENTILS</text>
  <line class="label-rule" x1="497" y1="784" x2="703" y2="784" stroke="var(--leaf)" stroke-width="1.5"/>
  <text class="label-text product-subname" x="600" y="818" text-anchor="middle" font-size="28"
        textLength="191" lengthAdjust="spacingAndGlyphs" fill="var(--leaf)">MASOOR DAL</text>

  <!-- certification badges -->
  <circle class="cert-badge" cx="781" cy="947" r="28" fill="var(--page)" stroke="var(--forest)" stroke-width="4"/>
  <rect class="cert-badge" x="820" y="924" width="71" height="44" fill="var(--cert-navy)"/>

  <!-- net weight -->
  <rect class="net-weight-box" x="514" y="994" width="167" height="26" fill="var(--leaf)"/>
  <text class="label-text net-weight" x="597" y="1014" text-anchor="middle" font-size="18"
        textLength="148" lengthAdjust="spacingAndGlyphs" fill="var(--page)">NET WT. 4lb</text>
</svg>
</body>
</html>
```